Consulting services and software brochure

We need a brochure designed that would ideally work with our logo and highlight a few of our consulting services and a couple products we offer. Our industry is real estate technology and we focus on consulting services for third party software systems. We would like the design to work well with our logo colors although we are open to changing either the blue or the orange to white in a design. The final design should clearly highlight our service options in an easy to read way while also leaving plenty of room to insert a lot of text on each service

What we like about our current design: it incorporates our colors well and has lots of room for text on each service, the two product offerings, and a couple testimonials from our clients

What we don’t like: It’s very busy and doesn’t highlight our offerings without a lot of reading. We also think it could have better layout, be much more polished and interesting visually (this was not designed by a professional).

Please provide source file compatible with Photoshop.

We are impressed with the designs so far and have made the payment guaranteed for this project. We will be starting to provide feedback early next week as we review internally.

Regarding size: We are open to a multi-page brochure or an 8 1/2 x 11, square shape, etc. After reviewing the designs we have decided the tri-folds seem to look too busy though on a standard piece of paper. Also, there's a good chance whatever designer we choose we will also hire to do another option in a different size/length so please don't worry either way too much about that.

Thanks for the great submissions so far!

Reason: Hi - we're extending the deadline a week since a few people providing input have been out this week for Passover and Good Friday. Thank you for your understanding.

Reason: Hi - we've settled on a designer and are now refining the brochure. Thank you everyone for your time and effort.

```html
<!DOCTYPE html>
<html lang="en">
<head>
<meta charset="utf-8">
<title>Keyline inc. brochure spread</title>
<link href="https://fonts.googleapis.com/css2?family=Carlito:ital,wght@0,400;0,700;1,400&family=Open+Sans:wght@400;600;700&display=swap" rel="stylesheet">
<style>
  :root {
    --indigo: #2e2d83;
    --indigo-text: #2f2b7c;
    --orange: #e8892d;
    --navy: #0f1f33;
    --paper: #ffffff;
    --backdrop: #e9e9ec;
    --ink: #1b1b1f;
    --divider: #d9d9de;
  }
  * { margin: 0; padding: 0; box-sizing: border-box; }
  html, body { width: 1200px; height: 785px; overflow: hidden; background: var(--backdrop); }
  body { font-family: "Open Sans", Arial, sans-serif; color: var(--ink); }

  .spread {
    position: absolute; left: 33px; top: 26px;
    width: 1133px; height: 732px;
    background: var(--paper);
    box-shadow: 0 2px 10px rgba(0,0,0,.18);
  }
  .block { position: absolute; }
  .bar-orange { background: var(--orange); }
  .bar-navy { background: var(--navy); }
  .panel-indigo { background: var(--indigo); }

  .page-fold { position: absolute; left: 566px; top: 578px; width: 1px; height: 154px; background: var(--divider); }

  /* testimonials */
  .testimonials { left: 38px; top: 0; width: 491px; height: 410px; padding: 15px 16px 0 13px; color: #fff;
    font-family: "Carlito", "Calibri", sans-serif; }
  .testimonial { margin-bottom: 22px; }
  .testimonial blockquote { font-weight: 700; font-size: 17.5px; line-height: 22.4px; }
  .testimonial cite { display: block; text-align: right; font-style: italic; font-size: 17.5px; line-height: 22.4px; }

  .skyline-photo { left: 38px; top: 417px; width: 491px; height: 161px;
    background: linear-gradient(180deg, #0d1e3c 0%, #1c3a6c 65%, #3a5f97 100%); }
  .team-photo { left: 605px; top: 114px; width: 491px; height: 296px;
    background: radial-gradient(ellipse at 55% 55%, #c7d8e8 0%, #8ea6bf 45%, #3a4b63 100%); }

  .headline { position: absolute; left: 606px; top: 77px; font-size: 24px; font-weight: 400; color: var(--indigo-text); }

  .services { left: 605px; top: 417px; width: 491px; height: 161px; padding: 6px 0 0 12px; list-style: none; color: #fff; }
  .services li { font-size: 19px; line-height: 21.3px; padding-left: 22px; position: relative; }
  .services li::before { content: ""; position: absolute; left: 1px; top: 7px; width: 9px; height: 9px; border-radius: 50%; background: #fff; }

  .contact { position: absolute; left: 33px; top: 616px; font-size: 14.5px; line-height: 18.8px; color: var(--orange); font-style: normal; }
  .contact-mark { position: absolute; left: 7px; top: 590px; width: 170px; height: 128px; background: var(--orange); opacity: .12; }

  .brand { position: absolute; display: flex; align-items: center; gap: 7px; }
  .brand-square { background: var(--navy); }
  .brand-name { font-weight: 700; color: var(--navy); letter-spacing: -.3px; }
  .brand--small { left: 348px; top: 654px; }
  .brand--small .brand-square { width: 16px; height: 16px; }
  .brand--small .brand-name { font-size: 22px; }
  .brand--large { left: 893px; top: 642px; }
  .brand--large .brand-square { width: 19px; height: 19px; }
  .brand--large .brand-name { font-size: 27px; }

  .phone { position: absolute; left: 605px; top: 684px; display: flex; align-items: center; gap: 13px; font-size: 18px; color: var(--ink); }
</style>
</head>
<body>
  <main class="spread">
    <!-- left page -->
    <div class="block bar-orange" style="left:0;top:0;width:32px;height:410px"></div>
    <section class="block panel-indigo testimonials">
      <figure class="testimonial">
        <blockquote>"No matter what the problems were, they always came back with viable solutions."</blockquote>
        <cite>-- Assistant Controller</cite>
      </figure>
      <figure class="testimonial">
        <blockquote>"Keyline was able to pick-up the existing program and enhance it to meet our new specifications... on-time and budget"</blockquote>
        <cite>-- Business Systems Manager</cite>
      </figure>
      <figure class="testimonial">
        <blockquote>"Beyond the initial implementation we have and will continue to utilize their experience and expertise."</blockquote>
        <cite>-- Treasurer</cite>
      </figure>
      <figure class="testimonial">
        <blockquote>"...the SheetBridge investment has a short payback period of a few months."</blockquote>
        <cite>-- Director of Finance</cite>
      </figure>
    </section>
    <div class="block bar-navy" style="left:534px;top:0;width:33px;height:410px"></div>

    <div class="block bar-navy" style="left:0;top:417px;width:32px;height:161px"></div>
    <div class="block skyline-photo" role="img" aria-label="Photo of glass residential towers against a deep blue evening sky with a row of palm trees"></div>
    <div class="block bar-orange" style="left:534px;top:417px;width:33px;height:161px"></div>

    <div class="contact-mark" aria-hidden="true"></div>
    <address class="contact">
      48 W. 27th St., Suite 410<br>
      New York, NY 10001<br>
      (646) 555-0142<br>
      hello@keylineinc.com<br>
      www.keylineinc.com
    </address>
    <div class="brand brand--small"><span class="brand-square"></span><span class="brand-name">Keyline inc.</span></div>

    <div class="page-fold"></div>

    <!-- right page -->
    <h1 class="headline">We understand Real Estate Technology</h1>
    <div class="block bar-orange" style="left:566px;top:114px;width:32px;height:296px"></div>
    <div class="block team-photo" role="img" aria-label="Photo of a businessman in a suit holding a laptop, tablet, phone and glowing globe connected by network lines"></div>
    <div class="block bar-navy" style="left:1101px;top:114px;width:32px;height:296px"></div>

    <div class="block bar-navy" style="left:566px;top:417px;width:32px;height:161px"></div>
    <ul class="block panel-indigo services">
      <li>Process Improvement,</li>
      <li>System Implementation,</li>
      <li>Data Conversion,</li>
      <li>Customization, Help Desk</li>
      <li>Support, Training,</li>
      <li>Spreadsheet Analytics,</li>
      <li>Dashboards/Business Intelligence</li>
    </ul>
    <div class="block bar-orange" style="left:1101px;top:417px;width:32px;height:161px"></div>

    <div class="phone">
      <svg width="20" height="20" viewBox="0 0 20 20" aria-hidden="true">
        <circle cx="10" cy="10" r="9" fill="none" stroke="#e8892d" stroke-width="1.4"/>
        <path d="M7 5.5 L8.6 5.2 L9.4 7.6 L8.4 8.4 C8.8 9.7 9.9 11 11.3 11.6 L12.2 10.6 L14.5 11.5 L14.2 13.1 C10.2 13.6 6.4 9.6 7 5.5 Z" fill="#e8892d"/>
      </svg>
      <span>(646) 555-0142</span>
    </div>
    <div class="brand brand--large"><span class="brand-square"></span><span class="brand-name">Keyline inc.</span></div>
  </main>
</body>
</html>
```